Maple Hollow Bloom Backdrops Business card

Looking to have a business card design incorporating my logo for my flower wall business.

Industry/Entity Type

Wedding & event planning

Contact Information for Business Card

My business logo, my name - Jill Worthing (owner), my tagline - Let us be your finishing bloom, phone # 401-627-3918, email address - maplehollowbloombackdrops@fernpost.com, my website - maplehollowbloombackdrops.com, Instagram handle- @maplehollowbloombackdrops, FB handle Handle - maplehollowbloombackdrops

Font styles to use
Other font styles liked:
• Sentaina is the font that is used in my logo

Requirements
Must have
• Would like a double sided business card

```html
<!DOCTYPE html>
<html lang="en">
<head>
<meta charset="utf-8">
<title>Maple Hollow Bloom Backdrops – Business Card</title>
<link href="https://fonts.googleapis.com/css2?family=Great+Vibes&family=Montserrat:wght@400;500&display=swap" rel="stylesheet">
<style>
  :root {
    --backdrop: #2d2d2e;
    --blush: #f4d9e4;
    --blush-deep: #e9c6d5;
    --paper: #f6f6f6;
    --ink: #1d1b1c;
    --gold: #d2b04c;
    --petal: #d98cc0;
    --disc: #f7f3f4;
  }
  * { margin: 0; padding: 0; box-sizing: border-box; }
  html, body { width: 1200px; height: 900px; overflow: hidden; }
  body {
    background: var(--backdrop);
    font-family: "Montserrat", sans-serif;
    color: var(--ink);
    position: relative;
  }
  .card {
    position: absolute;
    top: 65px;
    width: 440px;
    height: 770px;
    border-radius: 30px;
    overflow: hidden;
  }
  .card--front {
    left: 130px;
    background: radial-gradient(circle at 60% 55%, #fbe6ee 0%, var(--blush) 55%, var(--blush-deep) 100%);
  }
  .card--back {
    left: 630px;
    background: linear-gradient(160deg, #ffffff 0%, var(--paper) 60%, #e9e9e9 100%);
  }
  .brand-mark {
    position: absolute;
    left: 50%;
    transform: translateX(-50%);
    display: flex;
    align-items: center;
    justify-content: center;
    border-radius: 50%;
    text-align: center;
  }
  .card--front .brand-mark {
    top: 40px;
    width: 300px;
    height: 300px;
    background: var(--disc);
    box-shadow: inset 0 0 0 26px var(--disc), inset 0 0 0 28px var(--gold);
  }
  .card--back .brand-mark {
    top: 140px;
    width: 330px;
    height: 330px;
    box-shadow: inset 0 0 0 2px var(--gold);
  }
  .brand-name {
    font-family: "Montserrat", sans-serif;
    font-weight: 500;
    font-size: 24px;
    line-height: 1.35;
    letter-spacing: 0.04em;
    color: var(--ink);
    width: 210px;
  }
  .owner {
    position: absolute;
    top: 388px;
    left: 0;
    right: 0;
    text-align: center;
  }
  .owner-name {
    font-family: "Great Vibes", cursive;
    font-size: 64px;
    line-height: 1;
  }
  .owner-role {
    font-size: 17px;
    letter-spacing: 0.04em;
    margin-top: 2px;
    padding-left: 90px;
  }
  .divider {
    position: absolute;
    left: 30px;
    right: 30px;
    display: flex;
    align-items: center;
    gap: 8px;
  }
  .divider::before, .divider::after {
    content: "";
    flex: 1;
    height: 1.5px;
    background: var(--ink);
  }
  .divider--contact { top: 528px; }
  .divider--social { top: 650px; }
  .icon-dot {
    width: 30px;
    height: 30px;
    border-radius: 50%;
    background: var(--ink);
    display: flex;
    align-items: center;
    justify-content: center;
  }
  .icon-dot svg { width: 16px; height: 16px; }
  .details {
    position: absolute;
    left: 0;
    right: 0;
    text-align: center;
    font-size: 16px;
    line-height: 1.45;
  }
  .details--contact { top: 566px; }
  .details--social { top: 690px; }
  .tagline {
    position: absolute;
    bottom: 70px;
    left: 0;
    right: 0;
    text-align: center;
    font-size: 14px;
    letter-spacing: 0.08em;
    text-transform: uppercase;
  }
</style>
</head>
<body>

<section class="card card--front" aria-label="Business card front">
  <div class="brand-mark">
    <span class="brand-name">Maple Hollow Bloom Backdrops</span>
  </div>

  <div class="owner">
    <p class="owner-name">Jill Worthing</p>
    <p class="owner-role">OWNER</p>
  </div>

  <div class="divider divider--contact">
    <span class="icon-dot" aria-label="Phone">
      <svg viewBox="0 0 16 16"><path d="M4 2l2 3-1.3 1.3a8 8 0 0 0 5 5L11 10l3 2-1 2.5C7 15 1 9 1.5 3z" fill="var(--petal)"/></svg>
    </span>
    <span class="icon-dot" aria-label="Email">
      <svg viewBox="0 0 16 16"><rect x="1.5" y="3.5" width="13" height="9" rx="1" fill="var(--petal)"/><path d="M2 4l6 5 6-5" stroke="var(--ink)" stroke-width="1.2" fill="none"/></svg>
    </span>
    <span class="icon-dot" aria-label="Website">
      <svg viewBox="0 0 16 16" fill="none" stroke="var(--petal)" stroke-width="1.4"><circle cx="8" cy="8" r="6.2"/><ellipse cx="8" cy="8" rx="2.6" ry="6.2"/><path d="M2 8h12"/></svg>
    </span>
  </div>
  <div class="details details--contact">
    <p>401-627-3918</p>
    <p>maplehollowbloombackdrops@fernpost.com</p>
    <p>maplehollowbloombackdrops.com</p>
  </div>

  <div class="divider divider--social">
    <span class="icon-dot" aria-hidden="true"></span>
    <span class="icon-dot" aria-hidden="true"></span>
  </div>
  <div class="details details--social">
    <p>@maplehollowbloombackdrops</p>
    <p>maplehollowbloombackdrops</p>
  </div>
</section>

<section class="card card--back" aria-label="Business card back">
  <div class="brand-mark">
    <span class="brand-name">Maple Hollow Bloom Backdrops</span>
  </div>
  <p class="tagline">Let us be your finishing bloom</p>
</section>

</body>
</html>
```